Billboard for Lawyers who handle work accident cases

We need a billboard design for our law firm based in Queens, New York. The billboard is 8 by 10. The billboard is long and not wide.

Our firm focuses on work accidents. We are looking for a professional ad that will catch the attention of drivers and pedestrians passing by. The ad should be to the point.

I am attaching our picture and our logo for the ad. We like the idea of using the slogan "HURT AT WORK?" in English and Spanish "HERIDO EN EL TRABAJO?";

We want minimal writing on the billboard. Our telephone number should be included. The ad should say "Millions Recovered for our clients" It should also say "Attorney Advertisement" in small font in a discrete place. We would like use colors that match/coordinate the colors of our logo and/or picture but it is not required. The design should communicate serious/professional tone with a hint of modern/vibrant attorneys.

Once we have something to work with we will work with the designer for adjustments.

All people injured at work

Law Firm

• Must have HURT AT WORK and HERIDO EN EL TRABAJO (Spanish) OR another similar catchphrase
• Must have "Millions recovered for our clients"
• Must have telephone number (718) 555-0193
• Must have website "tqlegalteam.com"
• Must have in small font "Attorney Advertisement"

```html
<!DOCTYPE html>
<html lang="en">
<head>
<meta charset="utf-8">
<title>Torres &amp; Quinn – Hurt at Work Billboard</title>
<link rel="stylesheet" href="https://fonts.googleapis.com/css2?family=Oswald:wght@500;700&family=Roboto:wght@400;500&display=swap">
<style>
  :root {
    --stage: #acadac;
    --cream: #f2efe8;
    --cream-deep: #e4ddcd;
    --ink: #0d0d0d;
    --gold: #8b6f43;
    --tan: #c5b089;
    --red: #c21f2f;
    --red-bright: #e01b30;
    --navy: #1c2a4f;
    --caption: #e4e4e4;
  }
  html, body {
    margin: 0;
    padding: 0;
    width: 1200px;
    height: 1200px;
    overflow: hidden;
    background: var(--stage);
  }
  .stage {
    position: relative;
    width: 1200px;
    height: 1200px;
  }
  .billboard {
    position: absolute;
    left: 222px;
    top: 110px;
    width: 757px;
    height: 944px;
    display: block;
  }
  .headline { font-family: "Oswald", "Arial Narrow", sans-serif; font-weight: 700; }
  .firm-name { font-family: "Oswald", "Arial Narrow", sans-serif; font-weight: 500; }
  .body-text { font-family: "Roboto", Arial, sans-serif; }
  .size-caption {
    position: absolute;
    left: 0;
    width: 1200px;
    top: 1085px;
    text-align: center;
    font-family: "Roboto", Arial, sans-serif;
    font-size: 13px;
    color: var(--caption);
    letter-spacing: 0.2px;
  }
</style>
</head>
<body>
<div class="stage">
  <svg class="billboard" viewBox="0 0 757 944" xmlns="http://www.w3.org/2000/svg">
    <defs>
      <linearGradient id="backdropTone" x1="0" y1="0" x2="0" y2="1">
        <stop offset="0" stop-color="#efebe2"/>
        <stop offset="1" stop-color="#e6dfd0"/>
      </linearGradient>
      <linearGradient id="attorneyTone" x1="0" y1="0" x2="0" y2="1">
        <stop offset="0" stop-color="#d8bca5"/>
        <stop offset="0.5" stop-color="#c9a78e"/>
        <stop offset="0.62" stop-color="#2a3862"/>
        <stop offset="1" stop-color="#1c2a4f"/>
      </linearGradient>
    </defs>

    <!-- base -->
    <rect class="backdrop" x="0" y="0" width="757" height="944" fill="var(--cream)"/>

    <!-- tan footer band -->
    <path class="footer-band" d="M0 630 L63 665 L694 665 L757 630 L757 944 L0 944 Z" fill="var(--tan)"/>

    <!-- red side panels -->
    <path class="side-panel" d="M0 300 L63 300 L63 665 L0 630 Z" fill="var(--red)"/>
    <path class="side-panel" d="M694 250 L757 250 L757 630 L694 665 Z" fill="var(--red)"/>

    <!-- photo backdrop -->
    <rect class="photo-backdrop" x="63" y="300" width="631" height="582" fill="url(#backdropTone)"/>

    <!-- attorney portraits -->
    <rect class="portrait portrait-left" x="63" y="492" width="362" height="390" rx="4" fill="url(#attorneyTone)"
          role="img" aria-label="Photo of the first attorney in a navy suit with a red tie"/>
    <rect class="portrait portrait-right" x="374" y="486" width="320" height="396" rx="4" fill="url(#attorneyTone)"
          role="img" aria-label="Photo of the second attorney in a navy suit with a blue tie"/>

    <!-- cream headline field with curved red edge -->
    <path class="headline-field" d="M0 0 H757 V258 C660 440 520 508 379 510 C260 512 120 470 0 310 Z" fill="var(--cream)"/>
    <path class="headline-edge" d="M757 258 C660 440 520 508 379 510 C260 512 120 470 0 310" fill="none" stroke="var(--red-bright)" stroke-width="6"/>

    <!-- firm name -->
    <text class="firm-name" x="379" y="93" text-anchor="middle" font-size="24" fill="var(--gold)" letter-spacing="1">TORRES &amp; QUINN</text>

    <!-- headlines -->
    <text class="headline" x="123" y="186" font-size="82" fill="var(--ink)" textLength="512" lengthAdjust="spacingAndGlyphs">HURT AT WORK?</text>
    <text class="headline" x="123" y="234" font-size="50" font-weight="500" fill="var(--gold)" textLength="500" lengthAdjust="spacingAndGlyphs">HERIDO EN EL TRABAJO?</text>
    <text class="headline" x="215" y="318" font-size="80" fill="var(--red)" textLength="331" lengthAdjust="spacingAndGlyphs">MILLIONS</text>
    <text class="headline" x="215" y="386" font-size="64" fill="var(--red)" textLength="331" lengthAdjust="spacingAndGlyphs">RECOVERED</text>
    <text class="body-text" x="215" y="428" font-size="42" fill="var(--ink)" textLength="331" lengthAdjust="spacingAndGlyphs">FOR OUR CLIENTS</text>

    <!-- website -->
    <g class="website">
      <circle cx="381" cy="444" r="7" fill="var(--ink)"/>
      <path d="M374 444 H388 M381 437 V451 M375.5 440 H386.5 M375.5 448 H386.5" stroke="var(--cream)" stroke-width="1"/>
      <text class="body-text" x="392" y="450" font-size="19" fill="var(--ink)" textLength="154" lengthAdjust="spacingAndGlyphs">tqlegalteam.com</text>
    </g>

    <!-- footer text -->
    <text class="body-text" x="64" y="900" font-size="12" fill="var(--ink)">ATTORNEY ADVERTISEMENT</text>
    <g class="phone">
      <path d="M490 911 C489 902 496 893 505 890 L509 896 L504 899 C501 902 499 905 498 909 L492 912 Z" fill="var(--ink)"/>
      <text class="body-text" x="514" y="913" font-size="29" fill="var(--ink)" textLength="182" lengthAdjust="spacingAndGlyphs">(718) 555-0193</text>
    </g>
  </svg>
  <div class="size-caption">DESIGN SIZE : 8 FEET BY 10 FEET</div>
</div>
</body>
</html>
```